Ruler design for Brodmere Liquid waste

We require a very professional design for our marketing product 'Ruler'.
It will be on a white plastic ruler 315mm long and 39mm high.
0 – 30 on the top (in mm).
0 – 12 on the bottom (in inches).
Numbering in black (to be included as an example only) as it is already printed on the plastic stock.
I want logo, phone number, email and website.
Phone number - 08 8317 4925, email info@bwx.com.au, web www.brodmereliquidwaste.com
Large text - Your Local Grease Trap and Liquid Waste Specialists
Please stick to our colours.
Total workable text area –
Length 312mm
Height 24mm
You must supply Print ready pdf files with
all fonts embedded.
Please include crop marks plus 3mm bleed all round.
Marketing

```html
<!DOCTYPE html>
<html lang="en">
<head>
<meta charset="utf-8">
<title>Brodmere Liquid Waste – Ruler Strip</title>
<link href="https://fonts.googleapis.com/css2?family=Oswald:wght@600&family=Roboto:wght@400;500&display=swap" rel="stylesheet">
<style>
  :root {
    --bg: #cfcfcf;
    --navy: #221c52;
    --white: #ffffff;
    --orange: #f26b1d;
    --yellow: #f5d31b;
  }
  html, body {
    margin: 0;
    padding: 0;
    width: 1200px;
    height: 1000px;
    overflow: hidden;
    background: var(--bg);
  }
  .canvas {
    position: relative;
    width: 1200px;
    height: 1000px;
  }
  .ruler-strip {
    position: absolute;
    left: 76px;
    top: 460px;
    width: 1064px;
    height: 81px;
    background: var(--navy);
    box-shadow: 0 2px 6px rgba(0,0,0,0.25);
    font-family: "Roboto", Arial, sans-serif;
    color: var(--white);
  }
  .brand {
    position: absolute;
    left: 36px;
    top: 8px;
    width: 120px;
    text-align: center;
  }
  .brand-dot {
    display: block;
    width: 36px;
    height: 36px;
    margin: 0 auto 4px;
    border-radius: 50%;
    background: var(--orange);
  }
  .brand-name {
    font-family: "Roboto", Arial, sans-serif;
    font-weight: 500;
    font-size: 12px;
    letter-spacing: 1.5px;
    line-height: 13px;
    text-transform: uppercase;
    color: var(--white);
    margin: 0;
  }
  .message {
    position: absolute;
    left: 188px;
    top: 17px;
    width: 580px;
  }
  .headline {
    margin: 0;
    font-family: "Oswald", Impact, sans-serif;
    font-weight: 600;
    font-size: 27px;
    line-height: 32px;
    letter-spacing: 0.1px;
    white-space: nowrap;
    color: var(--white);
  }
  .services {
    display: flex;
    justify-content: space-between;
    width: 580px;
    margin: 3px 0 0;
    padding: 0;
    list-style: none;
    font-size: 10.5px;
    line-height: 13px;
    white-space: nowrap;
    color: var(--white);
  }
  .services li::before {
    content: "";
    display: inline-block;
    width: 6px;
    height: 6px;
    margin-right: 6px;
    vertical-align: 1px;
    background: var(--orange);
  }
  .contact {
    position: absolute;
    top: 30px;
    font-size: 10.5px;
    line-height: 14px;
    font-weight: 500;
    white-space: nowrap;
  }
  .contact-phones { left: 796px; }
  .contact-online { left: 888px; }
  .contact-divider {
    position: absolute;
    left: 879px;
    top: 31px;
    width: 2px;
    height: 28px;
    background: var(--yellow);
  }
  .contact-row {
    display: flex;
    align-items: center;
    gap: 5px;
  }
  .contact-row svg {
    width: 9px;
    height: 9px;
    fill: var(--orange);
  }
</style>
</head>
<body>
<div class="canvas">
  <section class="ruler-strip">
    <div class="brand">
      <span class="brand-dot"></span>
      <p class="brand-name">Brodmere<br>Liquid Waste</p>
    </div>

    <div class="message">
      <h1 class="headline">Your Local Grease Trap and Liquid Waste Specialists</h1>
      <ul class="services">
        <li>Grease trap service</li>
        <li>Trade waste cartage</li>
        <li>Winery waste water</li>
        <li>Oily water removal</li>
        <li>Septic and Aerobic cleaning</li>
      </ul>
    </div>

    <div class="contact contact-phones">
      <div class="contact-row">
        <svg viewBox="0 0 10 10" aria-hidden="true"><path d="M1 3.5C1 2 2.5 1 5 1s4 1 4 2.5L7.5 4.3 6.5 3H3.5L2.5 4.3z M2.5 5h5l1 4h-7z"/></svg>
        <span>08 8317 4925</span>
      </div>
      <div class="contact-row">
        <svg viewBox="0 0 10 10" aria-hidden="true"><path d="M2.5 1h5v2.5h-5z M1 4h8v4H7.5V6.5h-5V8H1z M3 7h4v2.5H3z"/></svg>
        <span>08 8317 5160</span>
      </div>
    </div>

    <div class="contact-divider"></div>

    <div class="contact contact-online">
      <div class="contact-row">
        <svg viewBox="0 0 10 10" aria-hidden="true"><path d="M1 2h8v6H1z" /><path d="M1 2l4 3.2L9 2" fill="none" stroke="#221c52" stroke-width="0.9"/></svg>
        <span>info@bwx.com.au</span>
      </div>
      <div class="contact-row">
        <svg viewBox="0 0 10 10" aria-hidden="true"><circle cx="5" cy="5" r="4.2"/><path d="M0.8 5h8.4M5 0.8v8.4M5 0.8c-2 2.5-2 5.9 0 8.4M5 0.8c2 2.5 2 5.9 0 8.4" fill="none" stroke="#221c52" stroke-width="0.7"/></svg>
        <span>www.brodmereliquidwaste.com</span>
      </div>
    </div>
  </section>
</div>
</body>
</html>
```